How likely are people to engage in social distancing? We need a good illustration to show the data!

We surveyed U.S. adults March 20th - 24th, 2020 and asked how likely they were to engage in social distancing (and other COVID-19 related health behaviors). What did the survey find? Basically, most people intend to engage in social distancing behaviors (e.g., avoiding large crowds) and other behaviors that reduce the spread of COVID-19 (e.g., washing hands at least 20 seconds). When most people intend to engage in a behavior, then public health professionals try to leverage that to move more people to act.
Now we need innovative and professional images that attempt to communicate one or all of these findings. The specific findings are nicely summarized in the attached document. For example, 82% of participants intend to engage in social distancing.
What sort of visual are we looking for? Our preference is for an original illustration (or set of illustrations). Our preference is for (creative and powerful illustrations, but we are also open to the creative and well-executed infographics.
We need these images fast . We will award monetary prizes to the 3 best designs. If we like more than that, then we might purchase more (e.g., in past contests, we have purchased as many as 30 designs).
What we will need:
(1) The illustrations must be original and we will need the photoshop and/or illustrator files for all artwork.
(2) You can illustrate all of the findings or just one of them. We need creative approaches that do a lucid job of bringing the data to life. Most people intend to engage in these behaviors. How to communicate that? Corvantists and Halmerites do not differ in their intentions; how to communicate that?
(3) The illustration should say, somewhere: "Based on a survey of 400 U.S. adults conducted March 20 - 24th, 2020."

U.S. Adults

• Original illustrations based on the findings of the survey (see attached document).

```html
<!DOCTYPE html>
<html lang="en">
<head>
<meta charset="utf-8">
<title>Behaviors to slow the spread of coronavirus</title>
<link href="https://fonts.googleapis.com/css2?family=Fira+Sans+Condensed:ital,wght@0,600;0,700;1,700&family=Fira+Sans:wght@800;900&family=Dancing+Script:wght@600&display=swap" rel="stylesheet">
<style>
:root{
  --navy:#2a3a83;
  --navy-dark:#13294b;
  --blue:#2f5fb3;
  --blue-text:#3d6cc2;
  --red:#ec2227;
  --red-title:#ef4130;
  --ink:#111;
  --title-grey:#3c3c3c;
  --panel:#e9edf0;
  --shade:#2b2b2b;
}
*{margin:0;padding:0;box-sizing:border-box}
html,body{width:978px;height:1200px;overflow:hidden;background:#fff}
.poster{position:relative;width:978px;height:1200px;font-family:"Fira Sans Condensed",sans-serif}
.survey-band{position:absolute;left:65px;top:2px;width:848px;height:58px;background:var(--navy);color:#fff;
  font-style:italic;font-weight:700;font-size:24px;display:flex;align-items:center;justify-content:center;letter-spacing:.2px}
.header{position:absolute;left:65px;top:60px;width:848px;height:290px;background:linear-gradient(#eef1f6,#fff 40%)}
.virus{position:absolute;border-radius:50%;background:radial-gradient(circle,#d4dae6 55%,rgba(212,218,230,0) 70%)}
.title{position:absolute;left:137px;font-family:"Fira Sans",sans-serif;font-weight:800;line-height:1}
.t1{top:84px;font-size:35px;color:var(--title-grey)}
.t2{top:130px;font-size:52px;color:var(--blue-text);letter-spacing:-1px;text-shadow:2px 2px 2px rgba(0,0,0,.3)}
.t3{top:192px;font-size:62px;color:var(--red-title);left:236px;letter-spacing:-1px;text-shadow:2px 2px 2px rgba(0,0,0,.3)}
.t3-the{position:absolute;left:148px;top:203px;font-family:"Dancing Script",cursive;font-size:32px;color:#111}
.t4{top:264px;font-size:62px;color:var(--red-title);letter-spacing:-1px;text-shadow:2px 2px 2px rgba(0,0,0,.3)}
.chart-panel{position:absolute;left:65px;top:350px;width:848px;height:744px;
  background:radial-gradient(ellipse at 50% 55%,#fbfcfd 0%,var(--panel) 70%,#d6dadd 100%)}
.map-area{position:absolute;left:110px;top:395px;width:700px;height:375px;border-radius:40px;
  background:radial-gradient(ellipse,rgba(160,160,160,.22),rgba(160,160,160,0) 70%)}
.legend{position:absolute;top:404px;left:303px;display:flex;align-items:center;font-weight:700;font-size:24px;color:#333}
.swatch{width:43px;height:24px;margin-right:18px}
.swatch.a{background:#4a86c8}
.swatch.b{background:var(--red-title);margin-left:30px}
.row{position:absolute;left:0;width:978px;height:48px}
.label{position:absolute;left:137px;top:0;height:48px;display:flex;align-items:center;font-weight:600;font-size:17px;line-height:1.3;color:var(--ink);text-transform:uppercase}
.bar{position:absolute;left:428px;height:15px;width:calc(var(--p) * 4.41px);box-shadow:2px 3px 0 var(--shade)}
.bar.h{top:0;background:var(--blue)}
.bar.c{top:23px;background:var(--red)}
.pct{position:absolute;font-weight:700;font-size:21px;left:calc(450px + var(--p) * 4.41px);text-shadow:1px 1px 0 #fff,2px 2px 1px rgba(0,0,0,.35)}
.pct.h{top:-7px;color:var(--blue-text)}
.pct.c{top:21px;color:var(--red)}
.summary-band{position:absolute;left:65px;top:1094px;width:848px;height:75px;background:var(--navy-dark);color:#fff;
  font-weight:700;font-size:27px;display:flex;align-items:center;justify-content:center;text-shadow:2px 2px 2px #000}
.footer-strip{position:absolute;left:65px;top:1169px;width:848px;height:31px;background:linear-gradient(#e4e6e8,#cfd2d4)}
</style>
</head>
<body>
<main class="poster">
  <div class="survey-band">Based on a survey of 400 U.S. adults conducted March 20 - 24th, 2020</div>

  <header class="header">
    <div class="virus" role="img" aria-label="Faint virus particle decoration" style="left:0;top:0;width:110px;height:110px"></div>
    <div class="virus" role="img" aria-label="Faint virus particle decoration" style="left:545px;top:65px;width:90px;height:90px"></div>
    <div class="virus" role="img" aria-label="Large faint virus particle decoration" style="left:710px;top:70px;width:150px;height:200px"></div>
    <div class="virus" role="img" aria-label="Faint virus particle decoration" style="left:600px;top:225px;width:110px;height:80px"></div>
  </header>
  <h1>
    <span class="title t1">How likely it is that you will perform these</span>
    <span class="title t2">behaviors to slow</span>
    <span class="t3-the">the</span>
    <span class="title t3">SPREAD OF</span>
    <span class="title t4">CORONAVIRUS ?</span>
  </h1>

  <section class="chart-panel"></section>
  <div class="map-area" role="img" aria-label="Dotted map of the United States in the background"></div>

  <div class="legend">
    <span class="swatch a"></span>HALMERITES
    <span class="swatch b"></span>CORVANTISTS
  </div>

  <div class="row" style="top:571px"><span class="label">Engage in social distancing</span>
    <span class="bar h" style="--p:81"></span><span class="pct h" style="--p:81">81%</span>
    <span class="bar c" style="--p:82"></span><span class="pct c" style="--p:82">82%</span></div>
  <div class="row" style="top:631px"><span class="label">Work from home</span>
    <span class="bar h" style="--p:65"></span><span class="pct h" style="--p:65">65%</span>
    <span class="bar c" style="--p:60"></span><span class="pct c" style="--p:60">60%</span></div>
  <div class="row" style="top:691px"><span class="label">Avoid large gatherings</span>
    <span class="bar h" style="--p:84"></span><span class="pct h" style="--p:84">84%</span>
    <span class="bar c" style="--p:85"></span><span class="pct c" style="--p:85">85%</span></div>
  <div class="row" style="top:750px"><span class="label">Cancel social activities</span>
    <span class="bar h" style="--p:80"></span><span class="pct h" style="--p:80">80%</span>
    <span class="bar c" style="--p:82"></span><span class="pct c" style="--p:82">82%</span></div>
  <div class="row" style="top:810px"><span class="label">Put distance between youself<br>and other people</span>
    <span class="bar h" style="--p:87"></span><span class="pct h" style="--p:87">87%</span>
    <span class="bar c" style="--p:84"></span><span class="pct c" style="--p:84">84%</span></div>
  <div class="row" style="top:870px"><span class="label">Wash hands for<br>atleast 20 seconds</span>
    <span class="bar h" style="--p:88"></span><span class="pct h" style="--p:88">88%</span>
    <span class="bar c" style="--p:87"></span><span class="pct c" style="--p:87">87%</span></div>
  <div class="row" style="top:931px"><span class="label">Use hand sanitizer</span>
    <span class="bar h" style="--p:84"></span><span class="pct h" style="--p:84">84%</span>
    <span class="bar c" style="--p:87"></span><span class="pct c" style="--p:87">87%</span></div>
  <div class="row" style="top:993px"><span class="label">Avoid touching your eyes,<br>nose &amp; mouth</span>
    <span class="bar h" style="--p:82"></span><span class="pct h" style="--p:82">82%</span>
    <span class="bar c" style="--p:80"></span><span class="pct c" style="--p:80">80%</span></div>

  <footer class="summary-band">What does this table show? No big differences. Basically the same patterns</footer>
  <div class="footer-strip"></div>
</main>
</body>
</html>
```